Redesign the content on our home page

Thanks for your designs thus far.

There have been a few requests for feedback, so I have mocked up another layout. I am happy with everything except the 6 boxes in the green square. This is the piece I need the perfect design for.
- What the boxes look like
- Icons to be used
- Colours
- etc

__________________________________________________________________

We have the basic layout for our homepage, the header and footer are done. Please see attached (Homepage)

Only design in PSD etc needed, no coding. Also, header and footer not needed either, only formatting and graphic design of home page content. See eps file for the information.

I need more information added to the homepage and displayed in an organised way and designed so it presents well.

Our slogan is "Travel Insurance made simple". Therefore the design needs to represent this by being a simple, clear and clean layout of information. Website visitors need to be able to access and digest the information fast and this is reliant on the design of the information.

Attached is a mock up with all of the information.

Please ask and questions you need to help with the design.

Target Market(s)

Mostly female, any age.

Industry/Entity Type

Travel

Number of Pages Required

1 page

Font styles to use
Other font styles liked:
• MetaPro

Colors
f37122
33a6d7
33b8a4
dbdbdb
606060

Requirements
Must have
• - Follow home page look and feel
• - Simple design
• - Fast for a visitor to digest the information
Nice to have
• Simple design. Webpage is responsive so elements should look good when scaled for mobile.
Should not have
• No new colours to be introduced then what is in the design already or selected below.
• No new fonts.

```html
<!DOCTYPE html>
<html lang="en">
<head>
<meta charset="utf-8">
<title>TripNest – Travel Insurance Made Simple</title>
<link href="https://fonts.googleapis.com/css2?family=Roboto:wght@300;400;500;700&display=swap" rel="stylesheet">
<style>
:root{
  --orange:#f37122;
  --orange-dark:#e0611a;
  --blue:#33a6d7;
  --teal:#33b8a4;
  --grey:#dbdbdb;
  --grey-light:#f2f2f2;
  --text:#606060;
  --white:#ffffff;
}
*{box-sizing:border-box;margin:0;padding:0}
html,body{width:1200px;height:2964px;overflow:hidden}
body{font-family:"Roboto",Arial,sans-serif;color:var(--text);background:var(--white);position:relative}
p{font-size:12px;line-height:1.6}

/* header */
.site-header{height:52px;display:flex;align-items:center;justify-content:space-between;padding:0 60px 0 60px;background:var(--white)}
.brand{display:flex;align-items:center;gap:8px;background:var(--white);padding:6px 10px;font-weight:700;font-size:22px;color:var(--orange)}
.brand-square{width:14px;height:14px;background:var(--orange)}
.header-right{text-align:right}
.header-phone{font-size:12px;color:var(--text)}
.main-nav{display:flex;gap:22px;font-size:11px;color:var(--orange);margin-top:4px}

/* hero */
.hero{position:relative;height:430px;background:var(--orange);overflow:hidden}
.hero-title{position:absolute;top:18px;width:100%;text-align:center;color:rgba(255,255,255,.6);font-size:12px}
.quote-line{position:absolute;left:0;width:100%;display:flex;justify-content:center;align-items:center;gap:14px;color:var(--white);font-size:40px;font-weight:300}
.quote-line.l1{top:48px}
.quote-line.l2{top:112px}
.field{background:var(--blue);color:var(--white);font-size:14px;border-radius:4px;height:44px;display:flex;align-items:center;justify-content:center;padding:0 14px}
.field.dest{width:190px;justify-content:space-between;background:var(--white);color:var(--text)}
.field.dest .dot{width:22px;height:22px;border-radius:50%;background:var(--blue)}
.field.date{width:60px;flex-direction:column;font-size:11px;line-height:1.2}
.field.date b{font-size:18px;font-weight:500}
.cta{position:absolute;top:190px;left:50%;transform:translateX(-50%);background:var(--blue);color:var(--white);font-size:13px;padding:12px 28px;border-radius:22px}
.hero-under{position:absolute;top:236px;width:100%;text-align:center;color:var(--white);font-size:12px}
.hero-arrow{position:absolute;top:130px;right:224px;width:40px;height:40px;border-radius:50%;background:rgba(0,0,0,.12)}
.hero-arrow svg{width:40px;height:40px}
.hero-scene{position:absolute;left:0;bottom:40px;width:100%;height:150px;background:linear-gradient(180deg,rgba(255,255,255,0) 0%,rgba(255,190,150,.45) 100%)}
.traveller{position:absolute;left:120px;bottom:60px;width:110px;height:270px;background:linear-gradient(180deg,#ffd0b0,#c2421a);border-radius:40px 40px 6px 6px}
.hero-curve{position:absolute;bottom:0;left:0;width:1200px;height:70px}

/* section heading */
.section-title{text-align:center;font-size:17px;font-weight:500;color:var(--text)}
.section-title::after{content:"";display:block;width:50px;height:2px;background:var(--orange);margin:10px auto 0}

/* benefits */
.benefits{position:absolute;top:590px;left:0;width:100%}
.benefit-grid{width:900px;margin:30px auto 0;display:grid;grid-template-columns:repeat(3,1fr);gap:24px 26px}
.benefit-card{background:var(--white);border:1px solid var(--grey);border-bottom:3px solid var(--teal);height:192px;text-align:center;padding:22px 22px 0}
.icon{width:46px;height:46px;border-radius:50%;background:var(--teal);margin:0 auto 12px;display:flex;align-items:center;justify-content:center}
.icon svg{width:24px;height:24px}
.benefit-card h3{font-size:13px;font-weight:500;color:var(--teal);margin-bottom:8px}
.benefit-card p{font-size:11px}

.divider{position:absolute;top:1076px;left:0;width:100%;height:4px;background:var(--orange)}
.divider::after{content:"";position:absolute;left:50%;top:4px;margin-left:-12px;border:12px solid transparent;border-top-color:var(--orange)}

/* award */
.award{position:absolute;top:1128px;width:100%}
.award-row{display:flex;justify-content:center;align-items:center;gap:20px;margin-top:24px}
.badge-shape{width:120px;height:42px;border-radius:21px;background:var(--teal)}
.award-row p{font-size:11px;color:var(--text)}

/* confidence */
.confidence{position:absolute;top:1316px;width:100%}
.confidence-intro{width:900px;margin:20px auto 0;text-align:center;font-size:11px}
.confidence-link{text-align:center;font-size:11px;color:var(--blue);margin-top:8px}
.trust-grid{width:900px;margin:22px auto 0;display:grid;grid-template-columns:repeat(4,1fr);gap:20px}
.trust-card{display:flex;gap:10px;align-items:flex-start}
.trust-badge{flex:0 0 70px;height:70px;border:1px solid var(--grey);display:flex;align-items:center;justify-content:center}
.trust-badge span{width:46px;height:46px;border-radius:50%;background:var(--orange)}
.trust-badge span.sq{border-radius:4px;background:var(--blue)}
.trust-card p{font-size:10px;line-height:1.5}

/* rating band */
.rating-band{position:absolute;top:1630px;left:0;width:100%;height:92px;background:var(--orange);color:var(--white);text-align:center;padding-top:28px}
.rating-band p{font-size:12px}
.stars{display:flex;justify-content:center;gap:4px;margin-top:8px}
.stars svg{width:14px;height:14px}

/* features */
.features{position:absolute;top:1764px;left:0;width:100%}
.feature-grid{width:860px;margin:0 auto;display:grid;grid-template-columns:repeat(3,1fr);gap:50px;text-align:center}
.feature h3{font-size:13px;font-weight:500;color:var(--teal);margin-bottom:8px}
.feature p{font-size:11px}

.city-scene{position:absolute;top:1980px;left:0;width:100%;height:180px;background:linear-gradient(180deg,#ffffff 0%,#ededed 100%)}
.city-traveller{position:absolute;top:1980px;left:560px;width:80px;height:170px;border-radius:30px 30px 4px 4px;background:linear-gradient(180deg,#f8b48a,#d9541b)}

/* stats */
.stats{position:absolute;top:2196px;left:0;width:100%}
.stat-grid{width:860px;margin:0 auto;display:grid;grid-template-columns:repeat(3,1fr);gap:30px}
.stat-card{display:flex;align-items:center;gap:14px;border:1px solid var(--grey);border-bottom:3px solid var(--teal);padding:22px 18px;height:116px}
.stat-card .icon{margin:0;flex:0 0 46px}
.stat-card h3{font-size:13px;font-weight:500;color:var(--teal);line-height:1.4}
.fine-print{position:absolute;top:2386px;width:100%;text-align:center}
.fine-print p{font-size:9px;color:#9a9a9a;width:860px;margin:0 auto}

/* footer */
.footer-main{position:absolute;top:2484px;left:0;width:100%;height:238px;background:var(--orange);color:var(--white)}
.footer-inner{width:900px;margin:0 auto;display:flex;gap:34px;padding-top:22px}
.footer-brand{width:200px;height:150px;background:var(--white);padding:18px 20px}
.footer-brand .brand{padding:0}
.footer-brand small{display:block;font-size:10px;color:var(--text);margin-top:4px}
.footer-brand .underwriter{margin-top:44px;font-size:14px;font-weight:700;color:var(--blue)}
.signup h4,.help h4{font-size:14px;font-weight:500;margin-bottom:10px}
.signup{width:240px}
.signup .input{height:26px;background:var(--white);border-radius:3px;margin-bottom:8px}
.signup .btn{width:90px;height:28px;border-radius:14px;background:var(--orange-dark);border:1px solid rgba(255,255,255,.6);font-size:11px;text-align:center;line-height:26px;margin:8px auto 0}
.help{width:170px}
.help p{font-size:11px;line-height:1.7}

.footer-links{position:absolute;top:2722px;left:0;width:100%;height:242px;background:var(--grey-light)}
.link-cols{width:900px;margin:0 auto;display:flex;gap:110px;padding:30px 0 0 170px}
.link-cols h5{font-size:11px;font-weight:500;color:var(--text);margin-bottom:6px}
.link-cols li{list-style:none;font-size:10px;color:var(--orange);line-height:1.6}
.legal{width:900px;margin:26px auto 0;text-align:center;font-size:8px;color:#9a9a9a;line-height:1.6}
</style>
</head>
<body>

<header class="site-header">
  <div class="brand"><span class="brand-square"></span>TripNest</div>
  <div class="header-right">
    <div class="header-phone">☎ 1300 555 014</div>
    <nav class="main-nav"><span>Travel Insurance</span><span>What we cover</span><span>Your Policy</span><span>FAQs</span><span>Emergency</span></nav>
  </div>
</header>

<section class="hero">
  <div class="hero-title">Get a fast travel insurance quote</div>
  <div class="quote-line l1">I'm travelling to <div class="field dest">Select <span class="dot"></span></div></div>
  <div class="quote-line l2">from <div class="field date">Sep<b>21</b></div> till <div class="field date">Month<b>&nbsp;</b></div></div>
  <div class="hero-arrow"><svg viewBox="0 0 40 40"><path d="M17 13l7 7-7 7" stroke="#fff" stroke-width="2.5" fill="none"/></svg></div>
  <div class="cta">I'm travelling multiple times in the year</div>
  <div class="hero-under">Underwritten by Brightshield</div>
  <div class="hero-scene" role="img" aria-label="Illustrated city skyline with suitcases"></div>
  <div class="traveller" role="img" aria-label="Illustrated traveller waving beside luggage"></div>
  <svg class="hero-curve" viewBox="0 0 1200 70" preserveAspectRatio="none"><path d="M0 70 Q600 -30 1200 70Z" fill="#fff"/></svg>
</section>

<section class="benefits">
  <h2 class="section-title">Travel Insurance Made Simple</h2>
  <div class="benefit-grid">
    <div class="benefit-card"><div class="icon"><svg viewBox="0 0 24 24"><path d="M5 12l5 5 9-10" stroke="#fff" stroke-width="2.5" fill="none"/></svg></div><h3>Fast &amp; Simple Instant Quotes</h3><p>Get a price in seconds with just a few details about your trip. No long forms, no waiting, simply choose your cover and go.</p></div>
    <div class="benefit-card"><div class="icon"><svg viewBox="0 0 24 24"><circle cx="12" cy="12" r="8" stroke="#fff" stroke-width="2" fill="none"/><path d="M12 7v5l3 3" stroke="#fff" stroke-width="2" fill="none"/></svg></div><h3>No Medical Assessment</h3><p>Many existing conditions are covered automatically, so you spend less time on paperwork and more time planning your trip.</p></div>
    <div class="benefit-card"><div class="icon"><svg viewBox="0 0 24 24"><path d="M12 3l7 3v6c0 4-3 7-7 9-4-2-7-5-7-9V6z" stroke="#fff" stroke-width="2" fill="none"/></svg></div><h3>A Simple PDS Format</h3><p>Our policy wording is written in plain language with clear headings, so you know exactly what is covered before you leave.</p></div>
    <div class="benefit-card"><div class="icon"><svg viewBox="0 0 24 24"><path d="M4 12h14M13 7l5 5-5 5" stroke="#fff" stroke-width="2.5" fill="none"/></svg></div><h3>Easy to Simple Purchase</h3><p>Buy online in a few clicks and receive your policy by email straight away. Pay securely and travel with peace of mind.</p></div>
    <div class="benefit-card"><div class="icon"><svg viewBox="0 0 24 24"><path d="M6 4h4l2 5-2.5 1.5a11 11 0 005 5L16 13l5 2v4a2 2 0 01-2 2A16 16 0 014 6a2 2 0 012-2z" fill="#fff"/></svg></div><h3>Fast Help</h3><p>Our friendly team is ready to help by phone or email, with emergency assistance available around the clock while you travel.</p></div>
    <div class="benefit-card"><div class="icon"><svg viewBox="0 0 24 24"><path d="M12 2a7 7 0 00-7 7c0 5 7 13 7 13s7-8 7-13a7 7 0 00-7-7z" fill="#fff"/><circle cx="12" cy="9" r="2.5" fill="#33b8a4"/></svg></div><h3>Simple Online Claims</h3><p>Lodge a claim online at any time, upload your receipts and track progress easily until your claim has been finalised.</p></div>
  </div>
</section>

<div class="divider"></div>

<section class="award">
  <h2 class="section-title">Award Winning Travel Insurance</h2>
  <div class="award-row">
    <div class="badge-shape" role="img" aria-label="Award badge"></div>
    <p>Best Value Comprehensive Cover<br>Best Value Budget Cover winner</p>
  </div>
</section>

<section class="confidence">
  <h2 class="section-title">Travel with Confidence</h2>
  <p class="confidence-intro">Our policies are backed by a leading global insurer with decades of experience. We cover thousands of travellers every year and keep our products simple, fair and easy to understand, so you can relax and enjoy every moment of your holiday abroad.</p>
  <p class="confidence-link">Read more about why we are trusted by travellers</p>
  <div class="trust-grid">
    <div class="trust-card"><div class="trust-badge" role="img" aria-label="Partner badge"><span></span></div><p>Recognised by an independent industry body for great value and clear product design.</p></div>
    <div class="trust-card"><div class="trust-badge" role="img" aria-label="Underwriter badge"><span class="sq"></span></div><p>Underwritten by Brightshield, a trusted global insurer with worldwide support.</p></div>
    <div class="trust-card"><div class="trust-badge" role="img" aria-label="Listing badge"><span></span></div><p>Listed as a top rated provider on a leading comparison service this year.</p></div>
    <div class="trust-card"><div class="trust-badge" role="img" aria-label="Certificate badge"><span class="sq"></span></div><p>Member of the national code of practice for general insurance providers.</p></div>
  </div>
</section>

<section class="rating-band">
  <p>Our travellers rate TripNest travel insurance <b>4.8 out of 5</b> from over <b>2,400 reviews</b></p>
  <div class="stars">
    <svg viewBox="0 0 24 24"><path d="M12 2l3 7h7l-5.5 4.5L18.5 21 12 16.5 5.5 21l2-7.5L2 9h7z" fill="#fff"/></svg>
    <svg viewBox="0 0 24 24"><path d="M12 2l3 7h7l-5.5 4.5L18.5 21 12 16.5 5.5 21l2-7.5L2 9h7z" fill="#fff"/></svg>
    <svg viewBox="0 0 24 24"><path d="M12 2l3 7h7l-5.5 4.5L18.5 21 12 16.5 5.5 21l2-7.5L2 9h7z" fill="#fff"/></svg>
    <svg viewBox="0 0 24 24"><path d="M12 2l3 7h7l-5.5 4.5L18.5 21 12 16.5 5.5 21l2-7.5L2 9h7z" fill="#fff"/></svg>
    <svg viewBox="0 0 24 24"><path d="M12 2l3 7h7l-5.5 4.5L18.5 21 12 16.5 5.5 21l2-7.5L2 9h7z" fill="#fff"/></svg>
  </div>
</section>

<section class="features">
  <div class="feature-grid">
    <div class="feature"><div class="icon"><svg viewBox="0 0 24 24"><path d="M12 3l7 3v6c0 4-3 7-7 9-4-2-7-5-7-9V6z" fill="#fff"/></svg></div><h3>Travel Alerts</h3><p>Stay informed with the latest travel warnings and advice for your destination before and during your trip.</p></div>
    <div class="feature"><div class="icon"><svg viewBox="0 0 24 24"><path d="M12 2a7 7 0 00-7 7c0 5 7 13 7 13s7-8 7-13a7 7 0 00-7-7z" fill="#fff"/></svg></div><h3>Travel Guide</h3><p>Handy tips on packing, visas, health and safety to help you prepare for a smooth and happy journey.</p></div>
    <div class="feature"><div class="icon"><svg viewBox="0 0 24 24"><path d="M5 12l5 5 9-10" stroke="#fff" stroke-width="2.5" fill="none"/></svg></div><h3>Travel Blog</h3><p>Stories, ideas and inspiration from fellow travellers to help you plan your next great adventure.</p></div>
  </div>
</section>

<div class="city-scene" role="img" aria-label="Faint illustrated city skyline"></div>
<div class="city-traveller" role="img" aria-label="Illustrated traveller with suitcases"></div>

<section class="stats">
  <div class="stat-grid">
    <div class="stat-card"><div class="icon"><svg viewBox="0 0 24 24"><path d="M12 2a7 7 0 00-7 7c0 5 7 13 7 13s7-8 7-13a7 7 0 00-7-7z" fill="#fff"/></svg></div><h3>Australia's Most Popular Destination is NZ</h3></div>
    <div class="stat-card"><div class="icon"><svg viewBox="0 0 24 24"><path d="M5 12l5 5 9-10" stroke="#fff" stroke-width="2.5" fill="none"/></svg></div><h3>40% Overseas travels are for a Holiday</h3></div>
    <div class="stat-card"><div class="icon"><svg viewBox="0 0 24 24"><circle cx="12" cy="12" r="8" stroke="#fff" stroke-width="2" fill="none"/><path d="M12 7v5l3 3" stroke="#fff" stroke-width="2" fill="none"/></svg></div><h3>$11 of Overseas Spending was for Holiday</h3></div>
  </div>
</section>

<div class="fine-print">
  <p>Figures are based on recent national travel statistics and are provided as a general guide only. Please read the policy wording carefully to check that the cover suits your needs before you buy. Conditions, limits and exclusions apply to all policies.</p>
</div>

<footer class="footer-main">
  <div class="footer-inner">
    <div class="footer-brand">
      <div class="brand"><span class="brand-square"></span>TripNest</div>
      <small>Travel insurance made simple</small>
      <div class="underwriter">Brightshield</div>
    </div>
    <div class="signup">
      <h4>Want travel tips &amp; freebies?<br>Join our newsletter!</h4>
      <div class="input"></div>
      <div class="input"></div>
      <div class="btn">Sign up</div>
    </div>
    <div class="help">
      <h4>Need a hand?</h4>
      <p>Contact us<br>1300 555 014<br>hello@tripnest.example<br>Mon–Fri 8am–6pm</p>
    </div>
    <div class="help">
      <h4>Making a claim?</h4>
      <p>Claims line<br>1300 555 027<br>claims@tripnest.example<br><br>Get claim status online</p>
    </div>
  </div>
</footer>

<footer class="footer-links">
  <div class="link-cols">
    <div><h5>Cover</h5><ul><li>Comprehensive Cover</li><li>Essentials Cover</li><li>Budget Cover</li><li>Multi Trip Cover</li><li>Domestic Cover</li><li>Senior Travellers</li></ul></div>
    <div><h5>Support</h5><ul><li>Make a Claim</li><li>Emergency Help</li><li>Policy Documents</li><li>Travel Alerts</li><li>Contact Us</li><li>Complaints</li></ul></div>
    <div><h5>About</h5><ul><li>Our Story</li><li>Blog</li><li>Privacy Policy</li><li>Terms of Use</li><li>Careers</li></ul></div>
  </div>
  <p class="legal">TripNest is a trading name of a licensed insurance agent. Insurance is issued by Brightshield. Any advice is general only and does not take into account your objectives, financial situation or needs. Please consider the product disclosure statement before deciding to buy. © TripNest. All rights reserved.</p>
</footer>

</body>
</html>
```